Mira Tails

im a dog walker, pet sitter and dog groomer. I can look after all pets from once a day pop in feeds of cats to small holdings and exotics. have 10 years experience in the industry. I can look after peoples dogs for the day while they are out or for longer if on holiday. I walk dogs when people are at work so the dogs get to have fun too. I do house sitting so all your animals are looked after together. you have designed my business cards and I wanted the 'mira tails' with the paw to be the same on the leaflets. I have spoken to printolane and they have sent a pdf file of business card and said it can be cropped. please let me know if this cant be done
im also a qualified canine hydrotherapist

Target Market(s)

pet owners

Industry/Entity Type

Pet

Requirements
Must have
• my phone number 07834562719
• email miratails@mailbox-example.co.uk
• area; Ashbridge Vale, Kelsmoor and surrounding areas
• I want it almost done as bullet points with the main things being the dog walking and the pet sitting.
Nice to have
• cartoon animals like business card not the cartoons with big eyes

```html
<!DOCTYPE html>
<html lang="en">
<head>
<meta charset="utf-8">
<title>Mira Tails – Leaflet</title>
<link rel="stylesheet" href="https://fonts.googleapis.com/css2?family=Mulish:ital,wght@1,400&family=Signika:wght@600&display=swap">
<style>
  :root {
    --page-bg: #ecebe8;
    --frame-grey: #3c3c3e;
    --paper-white: #f7f7f6;
    --sun-yellow: #e9bd4c;
    --ink: #1c1c1c;
    --brand-blue: #1ea6df;
    --bullet-purple: #8a5aab;
    --photo-green: #7c8f3c;
    --photo-gold: #e6c77a;
  }
  * { margin: 0; padding: 0; box-sizing: border-box; }
  html, body {
    width: 1200px; height: 900px; overflow: hidden;
    background: var(--page-bg);
  }
  .leaflet {
    position: absolute; left: 36px; top: 50px;
    width: 1128px; height: 800px;
    background: var(--frame-grey);
    box-shadow: 0 6px 18px rgba(0,0,0,0.25);
    overflow: hidden;
  }
  .leaflet-shapes { position: absolute; inset: 0; }
  .brand {
    position: absolute; left: 84px; top: 112px;
    display: flex; align-items: center; gap: 26px;
  }
  .brand-dot {
    width: 92px; height: 92px; border-radius: 50%;
    background: var(--sun-yellow);
  }
  .brand-name {
    font-family: "Signika", sans-serif; font-weight: 600;
    font-size: 92px; line-height: 1; color: var(--brand-blue);
  }
  .tagline {
    position: absolute; left: 54px; top: 305px;
    font-family: "Mulish", sans-serif; font-style: italic;
    font-size: 28px; letter-spacing: 0.5px; color: var(--ink);
  }
  .services {
    position: absolute; left: 54px; top: 372px; list-style: none;
    font-family: "Signika", sans-serif; font-weight: 600;
    font-size: 32px; color: var(--ink);
  }
  .services li {
    display: flex; align-items: center; gap: 14px; height: 43px;
  }
  .services li::before {
    content: ""; width: 18px; height: 18px; border-radius: 50%;
    background: var(--bullet-purple);
  }
  .contact {
    position: absolute; left: 54px; top: 606px; list-style: none;
    font-family: "Signika", sans-serif; font-weight: 600;
    color: var(--ink);
  }
  .contact li { display: flex; align-items: center; gap: 10px; }
  .contact .contact-line { font-size: 23px; height: 40px; }
  .contact .contact-area { font-size: 21px; line-height: 30px; margin-top: 4px; align-items: flex-start; }
  .contact-icon { width: 26px; height: 26px; flex: none; }
  .contact-area .contact-icon { height: 34px; margin-top: 6px; }
</style>
</head>
<body>
<main class="leaflet">
  <svg class="leaflet-shapes" width="1128" height="800" viewBox="0 0 1128 800">
    <defs>
      <linearGradient id="photo-tone" x1="0" y1="0" x2="0" y2="1">
        <stop offset="0" stop-color="var(--photo-gold)"/>
        <stop offset="0.45" stop-color="#b79a4c"/>
        <stop offset="1" stop-color="var(--photo-green)"/>
      </linearGradient>
    </defs>
    <rect class="paper" x="20" y="23" width="1108" height="754" fill="var(--paper-white)"/>
    <rect class="tagline-band" x="20" y="303" width="700" height="44" fill="var(--sun-yellow)"/>
    <path class="contact-panel" d="M20,600 C150,565 330,558 440,600 C540,645 610,720 670,777 L20,777 Z" fill="var(--sun-yellow)"/>
    <path class="curve-band" d="M880,0 C690,140 510,420 545,580 C570,690 630,765 660,800 L1128,800 L1128,0 Z" fill="var(--frame-grey)"/>
    <g role="img" aria-label="Photo of a beagle standing in sunlit grass">
      <path class="hero-photo" d="M945,0 C750,140 555,420 588,580 C612,690 680,765 712,800 L1128,800 L1128,0 Z" fill="url(#photo-tone)"/>
    </g>
  </svg>

  <div class="brand">
    <span class="brand-dot"></span>
    <span class="brand-name">Mira Tails</span>
  </div>

  <p class="tagline">10 years experience in animal industry</p>

  <ul class="services">
    <li>Dog walking</li>
    <li>Pet/House sitting</li>
    <li>Dog Grooming</li>
    <li>Small holder knowledge</li>
  </ul>

  <ul class="contact">
    <li class="contact-line">
      <svg class="contact-icon" viewBox="0 0 26 26" aria-hidden="true"><rect x="2" y="6" width="22" height="14" fill="none" stroke="var(--ink)" stroke-width="1.6"/><path d="M2,6 L13,15 L24,6" fill="none" stroke="var(--ink)" stroke-width="1.6"/></svg>
      miratails@mailbox-example.co.uk
    </li>
    <li class="contact-line">
      <svg class="contact-icon" viewBox="0 0 26 26" aria-hidden="true"><circle cx="13" cy="13" r="11" fill="none" stroke="var(--ink)" stroke-width="1.8"/><path d="M9,7 L11,7 L12,10 L10.5,11.5 C11.3,13.3 12.7,14.7 14.5,15.5 L16,14 L19,15 L19,17 C19,18 18,19 17,19 C12,18.5 7.5,14 7,9 C7,8 8,7 9,7 Z" fill="var(--ink)"/></svg>
      07834.562.719
    </li>
    <li class="contact-area">
      <svg class="contact-icon" viewBox="0 0 26 34" aria-hidden="true"><path d="M13,1 C6.5,1 2,6 2,12 C2,20 13,33 13,33 C13,33 24,20 24,12 C24,6 19.5,1 13,1 Z" fill="var(--ink)"/><circle cx="13" cy="12" r="4.5" fill="var(--sun-yellow)"/></svg>
      <span>Ashbridge Vale, Kelsmoor<br>&amp; Surrounding Areas</span>
    </li>
  </ul>
</main>
</body>
</html>
```